Tarvel Ridge LLC

Need Professional Business cards for New Investment Fund

Target Market(s)

High Quality investors

Industry/Entity Type

Financial

Contact Information for Business Card

Phone Number +1 555 284 6193
Name Pavel Orlinsky
Title Fund Manager
email po@FundTarvel.example
Website www.FundTarvel.example

Colors

Designer to choose colors to be used in the design.

Requirements
Must have
• Must have our Logo and all of the above. Must be made so lettering and loge can be raised

```html
<!DOCTYPE html>
<html lang="en">
<head>
<meta charset="utf-8">
<title>Tarvel Ridge LLC – Business Card</title>
<link rel="stylesheet" href="https://fonts.googleapis.com/css2?family=Open+Sans:wght@400;600;700&display=swap">
<style>
  :root {
    --page-bg: #e6e8e6;
    --card-white: #ffffff;
    --brand-green: #2bd31a;
    --brand-green-deep: #1fae12;
    --slate: #414a43;
    --slate-dark: #353d37;
    --text-grey: #4a4a4a;
    --back-green: #3f4a40;
    --back-pattern: #465246;
  }
  * { box-sizing: border-box; margin: 0; padding: 0; }
  html, body {
    width: 1200px; height: 1000px; overflow: hidden;
    background: var(--page-bg);
    font-family: "Open Sans", Arial, sans-serif;
  }
  .sheet { position: relative; width: 1200px; height: 1000px; }
  .card {
    position: absolute; left: 250px; width: 700px; height: 400px;
    overflow: hidden;
    box-shadow: 0 6px 20px rgba(0,0,0,0.18);
  }
  .card-front { top: 60px; background: var(--card-white); }
  .card-back { top: 540px; background: var(--back-green); }

  .card-bands { position: absolute; inset: 0; }

  .holder { position: absolute; left: 60px; top: 120px; }
  .holder-name {
    color: var(--brand-green); font-weight: 600; font-size: 24px;
    letter-spacing: 0.5px; text-transform: uppercase; line-height: 1.1;
  }
  .holder-title {
    color: var(--slate-dark); font-weight: 600; font-size: 17px; margin-top: 2px;
  }
  .divider {
    position: absolute; left: 60px; top: 186px; width: 400px; height: 2px;
    background: var(--brand-green);
  }
  .contact-list {
    position: absolute; left: 60px; top: 204px; list-style: none;
  }
  .contact-item {
    display: flex; align-items: center; gap: 10px;
    color: var(--text-grey); font-size: 16px; line-height: 24px;
  }
  .contact-icon { width: 14px; height: 14px; fill: var(--brand-green); }

  .brand-name {
    position: absolute; right: 50px; top: 258px;
    color: var(--slate); font-weight: 700; font-size: 34px;
    letter-spacing: 1px; text-transform: uppercase; white-space: nowrap;
  }

  .back-pattern {
    position: absolute; inset: 24px;
    background: var(--back-pattern);
  }
  .back-brand {
    position: absolute; right: 34px; bottom: 30px;
    display: flex; align-items: center; gap: 8px;
    color: #ffffff; font-weight: 700; font-size: 18px;
    text-transform: uppercase; letter-spacing: 1px;
  }
  .back-brand-mark { width: 12px; height: 12px; background: var(--brand-green); }
</style>
</head>
<body>
<main class="sheet">

  <section class="card card-front" aria-label="Business card front">
    <svg class="card-bands" width="700" height="400" viewBox="0 0 700 400" aria-hidden="true">
      <polygon points="30,0 700,0 700,14 30,14 30,22 0,0" fill="var(--slate)"/>
      <rect x="0" y="372" width="650" height="14" fill="var(--brand-green)"/>
      <polygon points="640,358 700,386 640,400 650,386" fill="var(--brand-green-deep)"/>
    </svg>

    <div class="holder">
      <h1 class="holder-name">Pavel Orlinsky</h1>
      <p class="holder-title">Fund Manager</p>
    </div>
    <div class="divider"></div>

    <ul class="contact-list">
      <li class="contact-item">
        <svg class="contact-icon" viewBox="0 0 16 16" aria-hidden="true"><path d="M3 1l3 3-2 2c1 2 3 4 5 5l2-2 3 3-2 3C6 15 1 10 0 3z"/></svg>
        +1 555 284 6193
      </li>
      <li class="contact-item">
        <svg class="contact-icon" viewBox="0 0 16 16" aria-hidden="true"><path d="M0 3h16v10H0z M0 3l8 6 8-6" stroke="#fff" stroke-width="1"/></svg>
        po@FundTarvel.example
      </li>
      <li class="contact-item">
        <svg class="contact-icon" viewBox="0 0 16 16" aria-hidden="true"><circle cx="8" cy="8" r="8"/><path d="M1 8h14M8 1v14" stroke="#fff" stroke-width="1"/></svg>
        www.FundTarvel.example
      </li>
    </ul>

    <p class="brand-name">Tarvel Ridge</p>
  </section>

  <section class="card card-back" aria-label="Business card back">
    <div class="back-pattern" role="img" aria-label="Embossed repeating brand pattern area"></div>
    <p class="back-brand"><span class="back-brand-mark"></span>Tarvel Ridge</p>
  </section>

</main>
</body>
</html>
```